Business Card Design

BBQ Concessions and Event Catering
Hi! My name is Dale I am looking for a biz card design for my BBQ company:
We specialize in ribs, brisket, pulled pork, chicken
Mainly Pork Product
Colors: Dark colors, Red, Black
Flames optional
This is a mobile trailer that moves to the party!
Copper Barn is a song by Lonnie Vasquell which influenced the name of my company. So I Love Blues and BBQ!
We also cater at music venues, parties, receptions etc. Anyone who needs good BBQ comes to us.

Looking forward to your designs.

Industry/Entity Type

Business

Contact Information for Business Card

Copper Barn BBQ, Dale Morrow Owner, 2718 Osgood Ave. LaPorte, In. 46912

```html
<!DOCTYPE html>
<html lang="en">
<head>
<meta charset="utf-8">
<title>Copper Barn BBQ – Business Card</title>
<link rel="stylesheet" href="https://fonts.googleapis.com/css2?family=Oswald:wght@300;400;500;700&display=swap">
<style>
  :root {
    --page-bg: #d9d6d2;
    --card-black: #0c0b0b;
    --ray-dark: #161414;
    --ray-light: #2a2727;
    --brand-red: #e0221f;
    --text-white: #f2efec;
  }
  * { margin: 0; padding: 0; box-sizing: border-box; }
  html, body {
    width: 1200px;
    height: 777px;
    overflow: hidden;
    background: var(--page-bg);
  }
  .stage {
    position: relative;
    width: 1200px;
    height: 777px;
    display: flex;
    align-items: center;
    justify-content: center;
  }
  .business-card {
    position: relative;
    width: 420px;
    height: 700px;
    background: var(--card-black);
    overflow: hidden;
    box-shadow: 0 8px 24px rgba(0,0,0,0.25);
    font-family: "Oswald", sans-serif;
  }
  .sunburst {
    position: absolute;
    inset: 0;
    width: 100%;
    height: 100%;
  }
  .contact-block {
    position: absolute;
    top: 40px;
    right: 44px;
    text-align: center;
    line-height: 1.1;
  }
  .contact-role {
    color: var(--brand-red);
    font-size: 22px;
    font-weight: 400;
    letter-spacing: 1px;
    text-transform: uppercase;
  }
  .contact-name,
  .contact-phone {
    color: var(--text-white);
    font-size: 28px;
    font-weight: 400;
    letter-spacing: 1px;
    text-transform: uppercase;
  }
  .brand-name {
    position: absolute;
    top: 170px;
    left: 80px;
    right: 30px;
    color: var(--brand-red);
    font-size: 82px;
    font-weight: 700;
    line-height: 0.95;
    text-transform: uppercase;
    text-align: center;
  }
  .brand-name span { display: block; }
  .service-block {
    position: absolute;
    top: 480px;
    left: 120px;
    line-height: 1.15;
    letter-spacing: 1px;
    text-transform: uppercase;
  }
  .service-line {
    color: var(--text-white);
    font-size: 29px;
    font-weight: 400;
  }
  .address-line {
    color: var(--brand-red);
    font-size: 29px;
    font-weight: 400;
  }
  .service-gap { height: 10px; }
</style>
</head>
<body>
  <main class="stage">
    <article class="business-card">
      <svg class="sunburst" viewBox="0 0 420 700" role="img" aria-label="Dark sunburst ray pattern radiating behind the brand name">
        <defs>
          <radialGradient id="sunburstGlow" cx="62%" cy="45%" r="70%">
            <stop offset="0%" stop-color="var(--ray-light)"/>
            <stop offset="55%" stop-color="var(--ray-dark)"/>
            <stop offset="100%" stop-color="var(--card-black)"/>
          </radialGradient>
        </defs>
        <rect width="420" height="700" fill="url(#sunburstGlow)"/>
      </svg>

      <section class="contact-block">
        <p class="contact-role">Owner</p>
        <p class="contact-name">Dale Morrow</p>
        <p class="contact-phone">219-555-0184</p>
      </section>

      <h1 class="brand-name">
        <span>Copper</span>
        <span>Barn</span>
        <span>BBQ</span>
      </h1>

      <section class="service-block">
        <p class="service-line">BBQ Concessions</p>
        <p class="service-line">&amp; Event Catering</p>
        <div class="service-gap"></div>
        <p class="address-line">2718 Osgood Ave.</p>
        <p class="address-line">LaPorte, In. 46912</p>
      </section>
    </article>
  </main>
</body>
</html>
```